Velmont Systems Business Card

Utilize the newly designed logo to create a polished, professional 2-sided business card for this IT Services company.

Target Market(s)

IT Professionals many in the telecommunications and medical industries.

Industry/Entity Type

Business

Requirements
Must have
• Use of new logo, identified color palette and font: Albertus MT Std Regular.

```html
<!DOCTYPE html>
<html lang="en">
<head>
<meta charset="utf-8">
<title>Velmont Systems Business Card</title>
<link rel="stylesheet" href="https://fonts.googleapis.com/css2?family=PT+Sans:wght@400;700&display=swap">
<style>
  :root {
    --sky: #00b8f1;
    --navy: #1e3f93;
    --brand: #2b3d8f;
    --mark: #6f8fd0;
    --paper: #ffffff;
    --edge: #333333;
    --rule: #6a7ab8;
    --label: #000000;
  }
  * { box-sizing: border-box; margin: 0; padding: 0; }
  html, body {
    width: 1200px; height: 360px; overflow: hidden;
    background: var(--paper);
    font-family: "PT Sans", Arial, sans-serif;
  }
  .canvas { position: relative; width: 1200px; height: 360px; }
  .side-label {
    position: absolute; top: 0; width: 446px; text-align: center;
    font-size: 13px; color: var(--label);
  }
  .side-label--front { left: 30px; }
  .side-label--back { left: 685px; }

  .card {
    position: absolute; top: 22px; width: 446px; height: 310px;
    border: 1px solid var(--edge); background: var(--paper); overflow: hidden;
  }
  .card--front { left: 30px; }
  .card--back { left: 685px; }

  /* Front */
  .front__band-top {
    position: absolute; left: 0; top: 0; width: 100%; height: 84px; background: var(--sky);
  }
  .front__band-bottom {
    position: absolute; left: 0; bottom: 0; width: 100%; height: 30px; background: var(--sky);
  }
  .front__halo {
    position: absolute; left: 146px; top: 70px; width: 160px; height: 160px;
    border-radius: 50%; background: var(--paper);
  }
  .front__person {
    position: absolute; right: 12px; top: 26px; text-align: right; color: var(--paper);
  }
  .front__name { font-size: 16px; line-height: 20px; }
  .front__title { font-size: 9px; line-height: 14px; margin-top: 4px; }
  .brand {
    position: absolute; left: 0; top: 110px; width: 446px; text-align: center;
    color: var(--brand); font-weight: 700;
  }
  .brand__dot {
    width: 72px; height: 72px; border-radius: 50%; background: var(--mark);
    margin: 0 auto 14px;
  }
  .brand__name { font-size: 24px; line-height: 26px; letter-spacing: 0.5px; }
  .brand__sub { font-size: 11px; line-height: 14px; letter-spacing: 0.8px; margin-top: 2px; }

  /* Back */
  .back__rule {
    position: absolute; left: 0; top: 79px; width: 100%; height: 1px; background: var(--rule);
  }
  .back__arc { position: absolute; left: 187px; top: 66px; }
  .back__panel {
    position: absolute; left: 0; top: 84px; width: 100%; height: 197px; background: var(--navy);
    color: var(--paper);
  }
  .back__address {
    position: absolute; left: 17px; top: 56px; font-size: 15px; line-height: 18px;
  }
  .contact {
    position: absolute; left: 226px; display: flex; align-items: center; gap: 10px;
    font-size: 14.5px; line-height: 18px;
  }
  .contact svg { width: 26px; height: 26px; flex: none; }
  .contact--phone { top: 48px; }
  .contact--mail { top: 84px; }
  .contact--web { top: 119px; }
</style>
</head>
<body>
<div class="canvas">
  <div class="side-label side-label--front">Front side</div>
  <div class="side-label side-label--back">Back side</div>

  <section class="card card--front">
    <div class="front__band-top"></div>
    <div class="front__halo"></div>
    <div class="front__band-bottom"></div>
    <div class="front__person">
      <div class="front__name">Anika R</div>
      <div class="front__title">Graphic Designer</div>
    </div>
    <div class="brand">
      <div class="brand__dot"></div>
      <div class="brand__name">VELMONT</div>
      <div class="brand__sub">SYSTEMS</div>
    </div>
  </section>

  <section class="card card--back">
    <div class="back__rule"></div>
    <svg class="back__arc" width="72" height="20" viewBox="0 0 72 20">
      <path d="M2 18 A40 40 0 0 1 70 18" fill="none" stroke="#00b8f1" stroke-width="2"/>
    </svg>
    <div class="back__panel">
      <div class="back__address">4820, Harbor Lane,<br>Brookfield</div>

      <div class="contact contact--phone">
        <svg viewBox="0 0 26 26" aria-hidden="true">
          <path d="M3 9 Q13 2 23 9 L21 12 L17 10 L17 8 Q13 6 9 8 L9 10 L5 12 Z" fill="#fff"/>
          <rect x="6" y="13" width="14" height="9" rx="1" fill="#fff"/>
          <circle cx="13" cy="17.5" r="2.5" fill="#1e3f93"/>
        </svg>
        <span>- 555-555-555-555</span>
      </div>

      <div class="contact contact--mail">
        <svg viewBox="0 0 26 26" aria-hidden="true">
          <rect x="3" y="7" width="20" height="13" fill="none" stroke="#fff" stroke-width="1.6"/>
          <path d="M3 7 L13 15 L23 7 M3 20 L10 13 M23 20 L16 13" fill="none" stroke="#fff" stroke-width="1.4"/>
        </svg>
        <span>- info@velmontsys.com</span>
      </div>

      <div class="contact contact--web">
        <svg viewBox="0 0 26 26" aria-hidden="true">
          <g fill="none" stroke="#fff" stroke-width="1.3">
            <circle cx="13" cy="13" r="9.5"/>
            <ellipse cx="13" cy="13" rx="4.5" ry="9.5"/>
            <path d="M13 3.5 V22.5 M3.5 13 H22.5 M5 8 H21 M5 18 H21"/>
          </g>
        </svg>
        <span>- www.velmontsys.com</span>
      </div>
    </div>
  </section>
</div>
</body>
</html>
```